fernbolt website

commerce website to sell cookeries, brackets, mailboxes and to show off homes built. Modern Steel in design see kelvo rides web page to be like: https://www.kelvorides.com/en/ sorry its blue mantis hosting word press divi

must be able to add products to page

Target Market(s)

mainly western states of U.S.

Industry/Entity Type

Building Product

Coding

Coded - Design and coding required

Number of Pages Required

3 page

Font styles to use
Sans Serif

Colors

Designer to choose colors to be used in the design.

Requirements
Must have
• customers to be able to order products from page
• blue mantis hosting word press divi

```html
<!DOCTYPE html>
<html lang="en">
<head>
<meta charset="utf-8">
<title>Fernbolt</title>
<link rel="stylesheet" href="https://fonts.googleapis.com/css2?family=Poppins:wght@400;500;600&family=Poiret+One&display=swap">
<style>
:root{
  --steel:#4f5f8a;
  --steel-light:#5c6c96;
  --ink:#2b2b2b;
  --body:#3a3a3a;
  --white:#ffffff;
  --charcoal:#333333;
  --sky-top:#9cc3ea;
  --sky-bottom:#dce9f4;
  --lawn:#4f6b3a;
}
*{margin:0;padding:0;box-sizing:border-box}
html,body{width:741px;height:1200px;overflow:hidden;background:var(--white)}
body{position:relative;font-family:"Poppins",sans-serif;color:var(--body)}
.abs{position:absolute}
.display{font-family:"Poiret One",sans-serif;color:var(--ink)}

.site-header{left:0;top:0;width:741px;height:70px;background:var(--steel)}
.brand{left:88px;top:18px;display:flex;align-items:center;gap:6px;color:var(--white);font-weight:500;font-size:17px;letter-spacing:.5px}
.brand-dot{width:14px;height:14px;border-radius:50%;background:var(--white)}
.top-contact{top:11px;display:flex;align-items:center;gap:5px;color:var(--white);font-size:9px}
.top-divider{left:523px;top:13px;width:1px;height:11px;background:rgba(255,255,255,.35)}
.main-nav{top:44px;color:var(--white);font-size:10px}
.main-nav.active{border-bottom:1.5px solid var(--white);padding-bottom:3px}

.hero{left:0;top:70px;width:741px;height:340px;background:linear-gradient(180deg,var(--sky-top) 0%,var(--sky-bottom) 45%,#8a8f88 70%,var(--lawn) 100%)}
.hero-caption{left:148px;top:305px;width:446px;height:105px;background:rgba(30,30,30,.45);text-align:center;color:var(--white);font-size:26px;line-height:39px;padding-top:12px}

.section-title{left:0;top:436px;width:741px;text-align:center;font-size:30px}
.rule{height:1.5px;background:var(--steel)}
.intro{left:80px;top:491px;width:581px;text-align:center;font-size:9.6px;line-height:17.5px}

.product-band{left:0;top:649px;width:741px;height:177px;background:var(--steel)}
.product-card{top:538px;width:159px;height:159px;background:var(--white);padding:5px;box-shadow:0 1px 4px rgba(0,0,0,.15)}
.product-photo{width:100%;height:100%}
.product-name{top:706px;width:180px;text-align:center;color:var(--white);font-size:13px;font-weight:500}
.product-rule{top:729px;width:30px;height:1.5px;background:var(--white)}
.product-text{top:738px;width:180px;text-align:center;color:var(--white);font-size:8px;line-height:14.5px}
.shop-button{left:294px;top:783px;width:128px;height:26px;border-radius:13px;background:var(--white);display:flex;align-items:center;padding-left:8px;gap:10px;color:var(--steel);font-weight:600;font-size:10px;letter-spacing:.3px}
.shop-dot{width:14px;height:14px;border-radius:50%;background:var(--steel)}

.goal{left:0;top:862px;width:741px;text-align:center;font-size:40px;line-height:51px}
.skyline{left:0;top:938px;width:741px;height:124px;background:linear-gradient(180deg,rgba(235,236,240,0) 0%,#eeeff2 40%,#e6e7eb 100%)}

.footer{left:0;top:1062px;width:741px;height:112px;background:var(--steel)}
.footer-nav-bar{left:0;top:1062px;width:741px;height:31px;background:var(--steel-light)}
.footer-nav{top:1069px;color:var(--white);font-size:8.6px}
.footer-nav.active{font-weight:600}
.footer-brand{left:109px;top:1128px;display:flex;align-items:center;gap:5px;color:var(--white);font-weight:500;font-size:14px}
.footer-brand .brand-dot{width:11px;height:11px}
.footer-divider{top:1118px;width:1px;height:36px;background:rgba(255,255,255,.3)}
.footer-contact{top:1125px;color:var(--white);font-size:8.6px;line-height:12.5px}
.footer-contact strong{font-weight:600}
.social{top:1127px;width:18px;height:18px;border-radius:50%;border:1px solid var(--white)}
.copyright{left:0;top:1174px;width:741px;height:26px;background:var(--charcoal);color:var(--white);font-size:7px;text-align:center;line-height:26px}
</style>
</head>
<body>

<header class="abs site-header"></header>
<div class="abs brand"><span class="brand-dot"></span>FERNBOLT</div>

<div class="abs top-contact" style="left:434px">
  <svg width="12" height="12" viewBox="0 0 24 24" fill="none" stroke="#fff" stroke-width="1.8"><path d="M5 3h4l2 5-3 2a12 12 0 0 0 6 6l2-3 5 2v4a2 2 0 0 1-2 2A17 17 0 0 1 3 5a2 2 0 0 1 2-2z"/></svg>
  480.555.0142
</div>
<div class="abs top-divider"></div>
<div class="abs top-contact" style="left:536px">
  <svg width="12" height="12" viewBox="0 0 24 24" fill="none" stroke="#fff" stroke-width="1.8"><rect x="3" y="6" width="18" height="13" rx="1"/><path d="M3 7l9 7 9-7"/></svg>
  inquiry@fernbolt.com
</div>

<nav>
  <div class="abs main-nav active" style="left:345px">Home</div>
  <div class="abs main-nav" style="left:397px">Products</div>
  <div class="abs main-nav" style="left:461px">Home Built</div>
  <div class="abs main-nav" style="left:534px">About Us</div>
  <div class="abs main-nav" style="left:599px">Contact Us</div>
</nav>

<section>
  <div class="abs hero" role="img" aria-label="Photograph of a large white farmhouse-style home with dark shingle roof, dormer windows and ivy, under a blue sky"></div>
  <div class="abs hero-caption display" style="color:var(--white)">We Sell Cookeries, Brackets, Mailboxes<br>And To Show Off Homes Built</div>
</section>

<section>
  <h2 class="abs section-title display" style="font-weight:400">Our Products</h2>
  <div class="abs rule" style="left:356px;top:480px;width:30px"></div>
  <p class="abs intro">Lorem ipsum dolor sit amet, consectetuer adipiscing elit, sed diam nonummy nibh euismod tincidunt ut laoreet dolore magna aliquam erat volutpat Ut wisi enim ad minim.</p>

  <div class="abs product-band"></div>

  <div class="abs product-card" style="left:94px"><div class="product-photo" role="img" aria-label="Photo of dark steel wall cladding beside a glass sliding door" style="background:linear-gradient(135deg,#2a2a2c,#5b5d60 60%,#3a3b3d)"></div></div>
  <div class="abs product-card" style="left:291px"><div class="product-photo" role="img" aria-label="Photo of a modern house with a steel-framed window box against a cloudy sky" style="background:linear-gradient(180deg,#7fa3cf 0%,#cfd8e3 45%,#8c8b87 75%,#a99a84 100%)"></div></div>
  <div class="abs product-card" style="left:491px"><div class="product-photo" role="img" aria-label="Photo of a raw steel outdoor cooker with a round top plate in a workshop" style="background:linear-gradient(180deg,#8b8f94 0%,#6d7075 40%,#2d2e31 75%,#9a9ca0 100%)"></div></div>

  <h3 class="abs product-name" style="left:83px">Steel Cookery</h3>
  <div class="abs product-rule" style="left:158px"></div>
  <p class="abs product-text" style="left:83px;top:741px">Lorem ipsum dolor sit amet, consectetuer adipiscing elit, sed diam</p>

  <h3 class="abs product-name" style="left:280px">Brackets</h3>
  <div class="abs product-rule" style="left:355px"></div>
  <p class="abs product-text" style="left:280px">Lorem ipsum dolor sit amet, consectetuer adipiscing elit, sed diam</p>

  <h3 class="abs product-name" style="left:480px">Mail Boxes</h3>
  <div class="abs product-rule" style="left:555px"></div>
  <p class="abs product-text" style="left:480px">Lorem ipsum dolor sit amet, consectetuer adipiscing elit, sed diam</p>

  <div class="abs shop-button"><span class="shop-dot"></span>SHOP NOW</div>
</section>

<section>
  <div class="abs skyline" role="img" aria-label="Faint grey illustration of a town skyline with churches and row houses"></div>
  <h2 class="abs goal display" style="font-weight:400">Our Goal Is Simply To Build<br>The Best Products In The World</h2>
</section>

<footer>
  <div class="abs footer"></div>
  <div class="abs footer-nav-bar"></div>
  <div class="abs footer-nav active" style="left:208px">Home</div>
  <div class="abs footer-nav" style="left:260px">Products</div>
  <div class="abs footer-nav" style="left:325px">Home Built</div>
  <div class="abs footer-nav" style="left:398px">About Us</div>
  <div class="abs footer-nav" style="left:464px">Contact Us</div>

  <div class="abs footer-brand"><span class="brand-dot"></span>FERNBOLT</div>
  <div class="abs footer-divider" style="left:223px"></div>
  <svg class="abs" style="left:251px;top:1126px" width="12" height="12" viewBox="0 0 24 24" fill="none" stroke="#fff" stroke-width="1.8"><rect x="3" y="6" width="18" height="13" rx="1"/><path d="M3 7l9 7 9-7"/></svg>
  <div class="abs footer-contact" style="left:268px"><strong>Email Us</strong><br>inquiry@fernbolt.com</div>
  <div class="abs footer-divider" style="left:401px"></div>
  <svg class="abs" style="left:430px;top:1126px" width="13" height="13" viewBox="0 0 24 24" fill="none" stroke="#fff" stroke-width="1.8"><path d="M5 3h4l2 5-3 2a12 12 0 0 0 6 6l2-3 5 2v4a2 2 0 0 1-2 2A17 17 0 0 1 3 5a2 2 0 0 1 2-2z"/></svg>
  <div class="abs footer-contact" style="left:452px"><strong>Call Us On</strong><br>480.555.0142</div>
  <div class="abs footer-divider" style="left:545px"></div>
  <div class="abs social" style="left:573px"></div>
  <div class="abs social" style="left:594px"></div>
  <div class="abs social" style="left:615px"></div>

  <div class="abs copyright">Copyright © 2020 Fernbolt. All Rights Reserved.</div>
</footer>

</body>
</html>
```